Lirevo Nocturna

Website for a night club with live music and cabaret dancers. I would like to have the following Menu: 1.) Home; 2) The Facilities; 3) The Show; 4) Other Attractions; 5) Videos & Fotos; 6) Program; 7) Reservations; 8) Membership; 9) Contacts.

The pages should be easily editable and allow to enter text, including the menu since the final version will be in both English and Portuguese. It should have a toggle or links for the Portuguese language and the English Language.

The night club itself is called "LIREVO NOCTURNA"; and its URL is www.lirevonocturna.example.

Industry/Entity Type

Night Club

```html
<!DOCTYPE html>
<html lang="en">
<head>
<meta charset="utf-8">
<title>Lirevo Nocturna</title>
<link href="https://fonts.googleapis.com/css2?family=Roboto:wght@300;400;500;700&display=swap" rel="stylesheet">
<style>
:root{
  --orange:#e9843a;
  --ink:#1c1d21;
  --bar:#1e1f24;
  --white:#ffffff;
  --text:#555555;
  --title:#8a1f2a;
}
*{margin:0;padding:0;box-sizing:border-box}
html,body{width:682px;height:1200px;overflow:hidden}
body{position:relative;font-family:"Roboto",Arial,sans-serif;color:var(--text);
  background:radial-gradient(ellipse at 20% 15%,#7a2a2a 0%,transparent 40%),
  radial-gradient(ellipse at 80% 25%,#4e5a1c 0%,transparent 40%),
  radial-gradient(ellipse at 30% 70%,#3b1e1e 0%,transparent 45%),
  radial-gradient(ellipse at 75% 95%,#6a2b22 0%,transparent 40%),
  linear-gradient(180deg,#2a1616 0%,#15120f 40%,#2a1a16 100%)}
.bg-photo{position:absolute;inset:0}
.abs{position:absolute}
.brand-mark{left:32px;top:18px;width:54px;height:54px;border-radius:50%;background:var(--orange)}
.brand-caption{left:32px;top:78px;font-size:8px;color:#fff}
.site-name{left:160px;top:34px;width:356px;text-align:center;font-size:34px;font-weight:500;color:var(--white);line-height:40px;white-space:nowrap}
.top-tools{left:518px;top:34px;display:flex;gap:3px}
.tool{width:21px;height:21px;background:#111;display:flex;align-items:center;justify-content:center}
.lang{width:22px;height:21px;background:var(--orange);color:#fff;font-size:8px;display:flex;align-items:center;justify-content:center}
.main-nav{left:32px;top:111px;width:627px;height:28px;background:var(--bar);display:flex}
.main-nav span{font-size:8px;color:#fff;font-weight:500;padding:0 11px;line-height:28px}
.main-nav .active{background:var(--orange)}
.hero-title{left:0;top:186px;width:682px;text-align:center;color:#fff;font-size:25px;font-weight:500}
.hero-text{left:0;top:221px;width:682px;text-align:center;color:#fff;font-size:19.5px;font-weight:300;line-height:30px;white-space:nowrap}
.hero-text span{background:rgba(0,0,0,.45);padding:0 3px}
.arrow{top:300px;width:21px;height:22px;background:#111;display:flex;align-items:center;justify-content:center}
.panel{background:#fff;box-shadow:0 1px 3px rgba(0,0,0,.4)}
.panel-head{height:42px;background:var(--orange);color:#fff;font-size:20px;font-weight:300;padding:10px 11px;position:relative}
.dots{position:absolute;right:11px;top:10px;width:22px;height:22px;border-radius:50%;background:#000;display:flex;align-items:center;justify-content:center;gap:2px}
.dots i{width:2px;height:2px;background:#fff;border-radius:50%}
.news-grid{display:grid;grid-template-columns:1fr 1fr}
.news-item{height:99px;padding:13px 10px;display:flex;gap:14px;border-right:1px solid #e6e6e6;border-bottom:1px solid #e6e6e6}
.thumb{flex:none;width:43px;height:43px;border-radius:50%;background:radial-gradient(circle at 40% 40%,#8a5aa0,#1a1020)}
.news-title{font-size:10px;color:var(--title);line-height:14px;margin-bottom:4px}
.news-text{font-size:7.5px;line-height:11.5px;color:#555}
.event-row{height:33px;display:flex;justify-content:space-between;align-items:center;padding:0 12px;font-size:11px;color:#222}
.day{background:var(--orange);color:#fff;font-size:8px;padding:2px 5px}
.gallery{display:grid;grid-template-columns:82px 82px;gap:8px 9px;padding:10px 11px}
.pic{height:62px;border:2px solid #fff;outline:1px solid #bbb}
.date-badge{width:42px;height:42px;border-radius:50%;background:#000;color:#fff;text-align:center;flex:none}
.cta{background:var(--orange);color:#fff;padding:12px 11px}
.band{left:32px;top:898px;width:627px;height:227px;background:var(--bar)}
.contact-body{padding:12px 10px;font-size:7.5px;line-height:11px;color:#333}
.social-grid{display:grid;grid-template-columns:repeat(5,26px);gap:4px 4px;padding:14px 0 0 21px}
.avatar{height:26px;background:#999}
.avatar-name{font-size:5px;text-align:center;color:#555}
.footer{left:32px;top:1145px;width:627px;height:33px;background:var(--bar);color:#fff;font-size:7.5px;text-align:right;padding:12px 11px}
</style>
</head>
<body>
<div class="bg-photo" role="img" aria-label="Blurred photo of cabaret dancers in feathered costumes"></div>

<header>
  <div class="abs brand-mark"></div>
  <div class="abs brand-caption">Lirevo Nocturna</div>
  <div class="abs site-name">Lirevo Nocturna</div>
  <div class="abs top-tools">
    <div class="tool"><svg width="9" height="9" viewBox="0 0 10 10"><circle cx="4" cy="4" r="3" fill="none" stroke="#fff" stroke-width="1.5"/><line x1="6.3" y1="6.3" x2="9" y2="9" stroke="#fff" stroke-width="1.5"/></svg></div>
    <div class="tool"></div><div class="tool"></div><div class="tool"></div>
    <div class="lang">En</div><div class="lang">Pt</div>
  </div>
  <nav class="abs main-nav">
    <span class="active">HOME</span><span>THE FACILITIES</span><span>THE SHOW</span><span>ATTRACTIONS</span><span>MEDIA</span><span>PROGRAM</span><span>RESERVATIONS</span><span>MEMBERSHIP</span><span>CONTACTS</span>
  </nav>
</header>

<section>
  <h1 class="abs hero-title">Burn Your Night</h1>
  <p class="abs hero-text"><span>From the moment you walk into Lirevo Nocturna until you leave,</span><br>we want your night to be the best of your life.</p>
  <div class="abs arrow" style="left:615px"><svg width="8" height="10"><path d="M6 1 2 5l4 4" fill="none" stroke="#fff" stroke-width="1.6"/></svg></div>
  <div class="abs arrow" style="left:638px"><svg width="8" height="10"><path d="M2 1l4 4-4 4" fill="none" stroke="#fff" stroke-width="1.6"/></svg></div>
</section>

<section class="abs panel" style="left:32px;top:365px;width:411px;height:240px">
  <div class="panel-head">Latest News<span class="dots"><i></i><i></i><i></i></span></div>
  <div class="news-grid">
    <div class="news-item"><div class="thumb" role="img" aria-label="Singer performing"></div><div><div class="news-title">Junk TVQ quiz graced</div><div class="news-text">Waltz, bad nymph, for quick jigs vex! Fox nymphs grab quick-jived waltz. Brick quiz whangs jumpy veldt fox. Bright...</div></div></div>
    <div class="news-item"><div class="thumb" role="img" aria-label="Drummer on stage"></div><div><div class="news-title">While the lovely valle</div><div class="news-text">I sink under the weight of the splendour of these visions!A wonderful serenity has taken possession of my entire...</div></div></div>
    <div class="news-item" style="border-bottom:0"><div class="thumb" role="img" aria-label="Dancer in costume"></div><div><div class="news-title">A wonderful serenity has taken possession</div><div class="news-text">A wonderful serenity has taken possession of my entire soul, like these sweet mornings of spring</div></div></div>
    <div class="news-item" style="border-bottom:0"><div class="thumb" role="img" aria-label="Band under stage lights"></div><div><div class="news-title">Would I could describe these conceptions</div><div class="news-text">who formed us in his own image, and the breath of that universal love which bears and sustains us,...</div></div></div>
  </div>
</section>

<section class="abs panel" style="left:464px;top:365px;width:195px;height:75px">
  <div class="panel-head">Events<span class="dots"><i></i><i></i><i></i></span></div>
  <div class="event-row"><span>SEPTEMBER 24, 2015</span><span class="day">Thu</span></div>
</section>

<section class="abs panel" style="left:464px;top:463px;width:195px;height:415px">
  <div class="panel-head">Gallery<span class="dots"><i></i><i></i><i></i></span></div>
  <div class="gallery">
    <div class="pic" role="img" aria-label="Wheat field" style="background:linear-gradient(#c9a24a,#8a6a26)"></div>
    <div class="pic" role="img" aria-label="Green field at sunset" style="background:linear-gradient(90deg,#4c7a22,#e2a73a)"></div>
    <div class="pic" role="img" aria-label="Black and white fence" style="background:linear-gradient(#c8c8c8,#555)"></div>
    <div class="pic" role="img" aria-label="Mountain lake" style="background:linear-gradient(#1d3f7a,#7fa8d8)"></div>
    <div class="pic" role="img" aria-label="Blueberries" style="background:radial-gradient(#4a5ab0,#1c2258)"></div>
    <div class="pic" role="img" aria-label="Red chili peppers" style="background:linear-gradient(#b82218,#5a120c)"></div>
    <div class="pic" role="img" aria-label="Green peas" style="background:radial-gradient(#8acb3c,#2f6a14)"></div>
    <div class="pic" role="img" aria-label="Tomatoes" style="background:radial-gradient(#e0462a,#7a1c10)"></div>
    <div class="pic" role="img" aria-label="Wheat field" style="background:linear-gradient(#c9a24a,#8a6a26)"></div>
    <div class="pic" role="img" aria-label="Green field at sunset" style="background:linear-gradient(90deg,#4c7a22,#e2a73a)"></div>
  </div>
</section>

<section class="abs panel" style="left:32px;top:628px;width:411px;height:138px">
  <div class="panel-head">Upcoming Events<span class="dots"><i></i><i></i><i></i></span></div>
  <div style="display:flex">
    <div style="width:205px;padding:14px 10px;display:flex;gap:17px">
      <div class="date-badge" style="margin-top:4px"><div style="font-size:16px;line-height:24px;padding-top:2px">24</div><div style="font-size:6px;line-height:6px">SEP</div></div>
      <div><div class="news-title">Madam Club Night</div><div class="news-text">Nullam quis dolor dui. Suspendisse ornare est et enim adipiscing sagittis. Donec turpis ante, euismod in mattis et, pellentesque...</div></div>
    </div>
    <div role="img" aria-label="Dancers in colourful feathered headdresses" style="margin:5px;width:196px;height:86px;background:linear-gradient(90deg,#1e2a12,#8a6a1c 40%,#a8302a 70%,#1a1a10)"></div>
  </div>
</section>

<section class="abs cta" style="left:32px;top:788px;width:411px;height:90px">
  <h2 style="font-size:20px;font-weight:300;line-height:26px">Burn Your Night</h2>
  <p style="font-size:12.5px;font-weight:300;line-height:20px">From the moment you walk into Lirevo Nocturna until you leave,<br>we want your night to be the best of your life.</p>
</section>

<div class="abs band"></div>

<section class="abs panel" style="left:32px;top:950px;width:195px;height:152px">
  <div class="panel-head">Contact Us</div>
  <div class="contact-body">
    <div style="color:var(--title);font-size:13px;line-height:16px;margin-bottom:2px">Lirevo Nocturna</div>
    <b>Street Name</b> - 18 Harbor Lane W., Northvale, QC. H0H0H0, Canada,<br><br>
    <b>Phone:</b> +1 555 010 0199<br><b>E-mail:</b> office@lirevonocturna.example<br><b>Website:</b> http://lirevonocturna.example
  </div>
</section>

<section class="abs panel" style="left:248px;top:950px;width:195px;height:148px">
  <div class="panel-head">Recent Photos</div>
  <div style="display:flex;gap:4px;padding:11px">
    <div role="img" aria-label="Dancer in costume" style="width:53px;height:80px;background:linear-gradient(#6a3a2a,#c47a3a)"></div>
    <div role="img" aria-label="Dancer with feather headdress" style="width:53px;height:80px;background:linear-gradient(#3a6a1a,#c8342a)"></div>
    <div role="img" aria-label="Dancer in white costume" style="width:53px;height:80px;background:linear-gradient(#2a2020,#d8d0c8)"></div>
  </div>
</section>

<section class="abs panel" style="left:464px;top:950px;width:195px;height:148px">
  <div class="panel-head">Social Widget</div>
  <div class="social-grid">
    <div><div class="avatar" style="background:#8aa8c8"></div><div class="avatar-name">Velmora</div></div>
    <div><div class="avatar" style="background:#6a7a5a"></div><div class="avatar-name">Rinaldo</div></div>
    <div><div class="avatar" style="background:#7a6a5a"></div><div class="avatar-name">Tiberio</div></div>
    <div><div class="avatar" style="background:#a84a3a"></div><div class="avatar-name">Oresta</div></div>
    <div><div class="avatar" style="background:#888"></div><div class="avatar-name">Kelo</div></div>
    <div><div class="avatar" style="background:#5a6a8a"></div><div class="avatar-name">Fenno</div></div>
    <div><div class="avatar" style="background:#9a8a7a"></div><div class="avatar-name">Lucan</div></div>
    <div><div class="avatar" style="background:#6a5a4a"></div><div class="avatar-name">Perla</div></div>
    <div><div class="avatar" style="background:#4a5a3a"></div><div class="avatar-name">Tamsin</div></div>
    <div><div class="avatar" style="background:#ddd"></div><div class="avatar-name">Vradek</div></div>
  </div>
</section>

<footer class="abs footer">Copyright © Lirevonocturna.example 2014. All Rights reserved.</footer>
</body>
</html>
```